Need a business cards for a hair dressing salon.

Target Market(s)

Target woman for Hair cuts, bridal makeup, occasion, fashion makeup and etc.

Industry/Entity Type

Hair

Font styles to use
Serif
Script

Requirements
Must have
• - Business card to be memorable and recognizable

- Please include the following on the business card:
- Business name: Salon Orimba
- Name: Kalini Desmodo (Name Must be changeable)
- Occupation: Hair Dresser & Beautician
- Contact number: 04 739 2 HAIR
- Email: mail@orimba.com.au
- Facebook (please use image): www.folkpage.net/orimba.com.au
Nice to have
• Font Styles:
Business Name - Script
Other Text - Serif

```html
<!DOCTYPE html>
<html lang="en">
<head>
<meta charset="utf-8">
<title>Salon Orimba – Business Card</title>
<link rel="stylesheet" href="https://fonts.googleapis.com/css2?family=Audiowide&family=Kaushan+Script&family=Jura:wght@500;600&display=swap">
<style>
  :root {
    --backdrop: #e4e4e6;
    --card-black: #0e0d0f;
    --card-black-soft: #1c1a1d;
    --pink: #e0378f;
    --pink-deep: #b81f6f;
    --pink-light: #f39ccb;
  }
  * { margin: 0; padding: 0; box-sizing: border-box; }
  html, body {
    width: 1200px;
    height: 750px;
    overflow: hidden;
    background: var(--backdrop);
  }
  .canvas {
    position: relative;
    width: 1200px;
    height: 750px;
  }
  .business-card {
    position: absolute;
    left: 180px;
    top: 135px;
    width: 840px;
    height: 480px;
    border-radius: 30px;
    overflow: hidden;
    background: radial-gradient(circle at 70% 30%, var(--card-black-soft), var(--card-black) 70%);
    box-shadow: 0 14px 30px rgba(0,0,0,0.18);
  }
  .portrait-art {
    position: absolute;
    left: 0;
    top: 0;
    width: 840px;
    height: 480px;
  }
  .salon-name {
    position: absolute;
    left: 300px;
    top: 42px;
    font-family: "Audiowide", sans-serif;
    font-weight: 400;
    font-size: 60px;
    letter-spacing: 1px;
    color: var(--pink);
    white-space: nowrap;
  }
  .stylist {
    position: absolute;
    left: 418px;
    top: 132px;
  }
  .stylist-name {
    font-family: "Kaushan Script", cursive;
    font-size: 46px;
    line-height: 1.1;
    color: var(--pink);
    white-space: nowrap;
  }
  .stylist-role {
    margin-top: 2px;
    margin-left: 6px;
    font-family: "Jura", sans-serif;
    font-weight: 600;
    font-size: 17px;
    color: var(--pink);
  }
  .contact-list {
    position: absolute;
    left: 424px;
    top: 232px;
    list-style: none;
  }
  .contact-item {
    display: flex;
    align-items: center;
    gap: 10px;
    height: 28px;
    font-family: "Jura", sans-serif;
    font-weight: 600;
    font-size: 17px;
    color: var(--pink);
    white-space: nowrap;
  }
  .contact-icon {
    width: 18px;
    height: 18px;
    flex: none;
  }
</style>
</head>
<body>
<main class="canvas">
  <article class="business-card">
    <svg class="portrait-art" viewBox="0 0 840 480" role="img" aria-label="Illustration of a woman with long flowing pink hair and a swirling pink wave along the lower edge">
      <defs>
        <linearGradient id="hairTone" x1="0" y1="0" x2="1" y2="1">
          <stop offset="0" stop-color="#f39ccb"/>
          <stop offset="0.5" stop-color="#e0378f"/>
          <stop offset="1" stop-color="#b81f6f"/>
        </linearGradient>
      </defs>
      <path fill="url(#hairTone)" d="M0 70 C60 40 150 50 210 110 C260 160 290 230 300 300 C380 330 470 350 560 400 C610 430 640 460 660 480 L0 480 Z"/>
    </svg>

    <h1 class="salon-name">Salon Orimba</h1>

    <div class="stylist">
      <p class="stylist-name">Kalini Desmodo</p>
      <p class="stylist-role">Hair Dresser &amp; Beautician</p>
    </div>

    <ul class="contact-list">
      <li class="contact-item">
        <svg class="contact-icon" viewBox="0 0 18 18" aria-hidden="true">
          <circle cx="9" cy="9" r="9" fill="var(--pink)"/>
          <path d="M6 4.5 L7.6 4.5 L8.3 6.8 L7.2 7.7 C7.8 9 8.9 10.2 10.3 10.8 L11.2 9.7 L13.5 10.4 L13.5 12 C13.5 12.8 12.8 13.5 12 13.4 C8.2 13 5 9.8 4.6 6 C4.5 5.2 5.2 4.5 6 4.5 Z" fill="var(--card-black)"/>
        </svg>
        04 739 2 HAIR
      </li>
      <li class="contact-item">
        <svg class="contact-icon" viewBox="0 0 18 18" aria-hidden="true">
          <circle cx="9" cy="9" r="9" fill="var(--pink)"/>
          <rect x="4.5" y="6" width="9" height="6.5" rx="1" fill="var(--card-black)"/>
          <path d="M4.8 6.4 L9 9.6 L13.2 6.4" fill="none" stroke="var(--pink)" stroke-width="1"/>
        </svg>
        mail@orimba.com.au
      </li>
      <li class="contact-item">
        <svg class="contact-icon" viewBox="0 0 18 18" aria-hidden="true">
          <circle cx="9" cy="9" r="9" fill="var(--pink)"/>
        </svg>
        www.folkpage.net/orimba.com.au
      </li>
    </ul>
  </article>
</main>
</body>
</html>
```